SkyvoraQ Business Cards and Stationary Design

Need a design for our business cards and stationary. I want to carry on the theme of the logo. I want the business cards to have a design on the back. I would like the business cards and the stationary to carry the same theme, design scheme, and branding

Target Market(s)

Airlines and Maintenance Facilities

Industry/Entity Type

Aviation

Contact Information for Business Card

Name
Position Title
Address: 4827 Tollbeck Lane, Fort Pierce, Florida, 34951
Office Number
Mobile Number
Email
Website

Font styles to use
Serif
Sans Serif

Colors

Designer to choose colors to be used in the design.

```html
<!DOCTYPE html>
<html lang="en">
<head>
<meta charset="utf-8">
<title>SkyvoraQ Letterhead</title>
<link rel="stylesheet" href="https://fonts.googleapis.com/css2?family=Montserrat:wght@700&family=Tinos&display=swap">
<style>
  :root {
    --navy: #1b2f50;
    --sky: #1b8fd0;
    --mist: #ebebeb;
    --ink: #111111;
    --paper: #ffffff;
  }
  html, body {
    margin: 0;
    padding: 0;
    overflow: hidden;
    background: var(--paper);
  }
  .letterhead {
    position: relative;
    width: 927px;
    height: 1200px;
    background: var(--paper);
    overflow: hidden;
  }
  .brand-mark {
    position: absolute;
    left: 417px;
    top: 47px;
    width: 90px;
    height: 90px;
    border-radius: 50%;
    background: var(--sky);
  }
  .brand-name {
    position: absolute;
    left: 0;
    right: 0;
    top: 146px;
    text-align: center;
    font-family: "Montserrat", sans-serif;
    font-weight: 700;
    font-size: 28px;
    letter-spacing: 7px;
    color: var(--navy);
    line-height: 1;
  }
  .rule {
    position: absolute;
    left: 48px;
    width: 831px;
    height: 0;
    border-top: 1.5px solid var(--navy);
  }
  .rule--top { top: 190px; }
  .rule--bottom { top: 1114px; }
  .contact-line {
    position: absolute;
    left: 0;
    width: 927px;
    height: 24px;
    font-family: "Tinos", serif;
    font-size: 18px;
    color: var(--ink);
    line-height: 24px;
  }
  .contact-line--top { top: 191px; }
  .contact-line--bottom { top: 1121px; }
  .contact-line span {
    position: absolute;
    white-space: nowrap;
  }
  .backdrop-emblem {
    position: absolute;
    left: 229px;
    top: 370px;
    width: 460px;
    height: 460px;
  }
</style>
</head>
<body>
  <main class="letterhead">
    <header>
      <div class="brand-mark" aria-hidden="true"></div>
      <div class="brand-name">SKYVORAQ</div>
      <div class="rule rule--top"></div>
      <div class="contact-line contact-line--top">
        <span style="left:162px">4827 Tollbeck Lane</span>
        <span style="left:381px">Fort Pierce, FL 34951</span>
        <span style="left:601px">www.skyvoraq.com</span>
      </div>
    </header>

    <svg class="backdrop-emblem" viewBox="0 0 460 460" aria-hidden="true">
      <circle cx="230" cy="230" r="212" fill="none" stroke="var(--mist)" stroke-width="33"/>
      <text x="230" y="244" text-anchor="middle" font-family="Montserrat, sans-serif" font-weight="700" font-size="46" letter-spacing="6" fill="var(--mist)">SKYVORAQ</text>
    </svg>

    <footer>
      <div class="rule rule--bottom"></div>
      <div class="contact-line contact-line--bottom">
        <span style="left:165px">Phone: 772.555.0148</span>
        <span style="left:392px">Fax: 772.555.0193</span>
        <span style="left:598px">info@skyvoraq.com</span>
      </div>
    </footer>
  </main>
</body>
</html>
```